Website Redesign - Spa Barn Depot

We need a new website for a hot tub dealer. This is a redesign of the existing site. The goal of the site is to drive phone calls and emails to book warehouse viewings, not to sell inventory from the website. The dealer sells both new and used hot tubs. I'd like to see some of the big name brands reflected; he's a small dealer and needs trust factor. He also has a great rating with QTR. We are no longer going to use the site to list inventory. This is a lead generation site. The existing site is boring. We would like to see some imagination. The client has a rustic back woods warehouse. He's a very knowledgeable yet quirky client. He doesn't want people showing up thinking that this is a big box fancy dealership. He's like the Bulkmart warehouse of hot tub dealers and the site should reflect that. No frills, honest advice, etc. www.spabarndepot.example

Target Market(s)

Surrey, Langley, Vancouver and area homeowners looking for new and used hot tubs

Number of Pages Required

5+ page

Font styles to use
Serif
Sans Serif

Colors

Designer to choose colors to be used in the design.

Requirements
Must have
• Home page

```html
<!DOCTYPE html>
<html lang="en">
<head>
<meta charset="utf-8">
<title>Spa Barn Depot – New and Used Hot Tubs</title>
<link rel="stylesheet" href="https://fonts.googleapis.com/css2?family=Arimo:wght@400;700&display=swap">
<style>
  :root {
    --navy: #29297d;
    --logo: #1f2f8c;
    --ink: #222222;
    --white: #ffffff;
    --field-line: #d6d6d6;
    --placeholder: #c4c4c4;
    --wave-1: #f1f1f1;
    --wave-2: #e8e8e8;
  }
  * { box-sizing: border-box; margin: 0; padding: 0; }
  html, body { width: 1200px; height: 1200px; overflow: hidden; background: var(--white); }
  body { position: relative; font-family: "Arimo", Arial, sans-serif; color: var(--ink); }

  .brand-name { position: absolute; left: 182px; font-size: 28px; font-weight: 700; color: var(--logo); letter-spacing: -0.3px; }

  .site-header .brand-name { top: 14px; }
  .main-nav { position: absolute; top: 31px; font-size: 13px; }
  .main-nav a { position: absolute; color: var(--ink); text-decoration: none; white-space: nowrap; }
  .header-edge { position: absolute; left: 1042px; top: 0; width: 1px; height: 68px; background: #555; }

  .hero { position: absolute; left: 157px; top: 68px; width: 886px; height: 430px; }
  .hero-photo { position: absolute; inset: 0; background: linear-gradient(110deg, #2e2e2e 0%, #4a4a4a 40%, #3a3a3a 70%, #2a2a2a 100%); }
  .hero-title { position: absolute; left: 55px; top: 164px; color: var(--white); font-size: 55px; font-weight: 700; line-height: 62px; }

  .contact-card { position: absolute; left: 560px; top: 69px; width: 287px; height: 309px; background: var(--white); border-radius: 6px; }
  .contact-card h2 { position: absolute; left: 0; right: 0; top: 28px; text-align: center; font-size: 34px; font-weight: 700; }
  .field { position: absolute; left: 27px; width: 222px; height: 20px; border-bottom: 1px solid var(--field-line); font-size: 13px; line-height: 15px; color: var(--placeholder); padding: 0 0 4px 5px; }
  .submit { position: absolute; left: 29px; top: 236px; width: 220px; height: 34px; border-radius: 5px; background: var(--navy); color: var(--white); font-size: 13px; text-align: center; line-height: 34px; }

  .brands { position: absolute; left: 0; top: 498px; width: 1200px; height: 300px; }
  .brand-waves { position: absolute; left: 157px; top: 200px; }
  .brands h2 { position: absolute; left: 210px; top: 74px; font-size: 34px; font-weight: 700; }
  .brands-lead { position: absolute; left: 211px; top: 132px; font-size: 19px; font-weight: 700; line-height: 23.5px; }
  .brand-list { position: absolute; top: 75px; font-size: 16px; line-height: 19.5px; }
  .brand-list.new { left: 547px; }
  .brand-list.used { left: 809px; }

  .appointment { position: absolute; left: 157px; top: 798px; width: 886px; height: 299px; background: var(--navy); color: var(--white); }
  .appointment h2 { position: absolute; left: 56px; top: 62px; font-size: 32px; font-weight: 700; line-height: 39px; }
  .appointment p { position: absolute; left: 56px; top: 187px; font-size: 19px; line-height: 23.5px; }
  .contact-line { position: absolute; left: 530px; font-weight: 700; white-space: nowrap; }
  .contact-line.phone { top: 160px; font-size: 25px; }
  .contact-line.email { top: 199px; font-size: 26px; }

  .site-footer .brand-name { top: 1130px; }
  .social { position: absolute; top: 1140px; font-size: 13px; }
  .social span { position: absolute; white-space: nowrap; }
  .social .label { font-weight: 700; }
</style>
</head>
<body>

<header class="site-header">
  <div class="brand-name">Spa Barn Depot</div>
  <nav class="main-nav">
    <a style="left:716px">Home</a>
    <a style="left:794px">About us</a>
    <a style="left:875px">Services
      <svg width="9" height="7" viewBox="0 0 9 7" style="margin-left:2px"><path d="M1 1.5 L4.5 5 L8 1.5" fill="none" stroke="#222" stroke-width="2"/></svg></a>
    <a style="left:978px">Blogs</a>
  </nav>
  <div class="header-edge"></div>
</header>

<section class="hero">
  <div class="hero-photo" role="img" aria-label="Dimmed photo of a freestanding tub beside a stone wall with a potted palm"></div>
  <h1 class="hero-title">Get new and<br>used hot tubs</h1>
  <form class="contact-card">
    <h2>Contact form</h2>
    <div class="field" style="top:100px">Name</div>
    <div class="field" style="top:142px">Email</div>
    <div class="field" style="top:187px">Subject</div>
    <div class="submit">Submit</div>
  </form>
</section>

<section class="brands">
  <svg class="brand-waves" width="886" height="100" viewBox="0 0 886 100" aria-hidden="true">
    <path d="M0 100 C120 40 300 20 420 28 C560 40 640 80 700 100 Z" fill="var(--wave-1)"/>
    <path d="M268 100 C380 40 520 0 640 8 C740 16 820 60 886 84 L886 100 Z" fill="var(--wave-1)"/>
    <path d="M268 100 C340 62 400 40 470 30 C560 45 630 80 700 100 Z" fill="var(--wave-2)"/>
  </svg>
  <h2>Hot Tub Brands</h2>
  <p class="brands-lead">Over 250 model options,<br>both new and used, from<br>over two dozen brands!</p>
  <p class="brand-list new">Authorized Dealer for<br>Cedar Spas | Daybreak<br>Stillwater | Alder Cove |<br>Far Shore | Prime Repose |<br>Summitline | Coast-to-Peak |<br>Haven | Plane Two |<br>Fieldman | Novara | Openstream.</p>
  <p class="brand-list used">Used hot tubs may be from<br>these brands or<br>BUBBLARI | Sunreel |<br>Easy-Rest | Heritage |<br>Polar | Tidewater |<br>Shoreline Spas | Badger Spas |<br>Prairia | Driftwalker |<br>Aqua Spas | Vexa | Serene |<br>Endless | Newt and more!</p>
</section>

<section class="appointment">
  <h2>Schedule an<br>appointment<br>by email or call</h2>
  <p>Come by for a viewing of our wide<br>range of new and used Hot Tubs.</p>
  <div class="contact-line phone">604-555-0142</div>
  <div class="contact-line email">sbdepot@mail.example</div>
</section>

<footer class="site-footer">
  <div class="brand-name">Spa Barn Depot</div>
  <div class="social">
    <span class="label" style="left:610px">Follow us on</span>
    <span style="left:738px">Friendwall</span>
    <span style="left:834px">Workline</span>
    <span style="left:920px">Snapreel</span>
  </div>
</footer>

</body>
</html>
```